Packaging Label Design for Eyelash Extension Adhesive

I need labels designed for my new adhesive I just came out with. This is adhesive for eyelash extensions. I already have my logo and love it and want it incorporated in the label.
This is Medical Grade Very low fume adhesive geared towards sensitive clients but yet so great it can be your regular adhesive for everyone not just your sensitive clients.
The attached files I did myself and I do actually really Love but want it tweaked and more professional lookin and smooth out the lines etc.... it looks grainey and want it crisp and clear. The two design I created are the look and feel for my business.

Target Market(s)

Licensed beauty professionals, certified Lash Artist

Industry/Entity Type

Business

Font styles to use
Sans Serif
Decorative
Script

Colors
6b449b

Requirements
Must have
• My Corvina Brow logo, the colors plum and white
• the fonts and look of label to be elegant & stylish
• I love the bracket { } look with ribbon behind it like wrapped around the bottle of adhesvive. which is only 10ml so it is a fairly small bottle
• ***FORGOT TO ADD THAT NEEDS THE LABEL TO EITHER HAVE A FRONT AND BACK 2 SEPERATE STICKERS OR JUST 1 LONG LABEL TO WRAP AROUND THE 10ML BOTTLE, NEED TO ADD INGREDIENTS AND MY BUSINESS INFO ON BACK OF LABEL. IF ONE LABEL IT NEEDS TO BE 1.25"HEIGHT X 3.40" LONG OR 1.25" X 1.5 TWICE

```html
<!DOCTYPE html>
<html lang="en">
<head>
<meta charset="utf-8">
<title>Corvina Brow – Lumen Soft Adhesive Label</title>
<link rel="stylesheet" href="https://fonts.googleapis.com/css2?family=Tinos&family=Playfair+Display+SC:wght@700&family=Josefin+Sans:wght@300&family=Great+Vibes&display=swap">
<style>
  :root {
    --plum: #6b449b;
    --plum-deep: #5a3787;
    --plum-light: #9a78c4;
    --panel: #f2f1f4;
    --panel-edge: #a9a7ad;
    --white: #ffffff;
    --page: #ffffff;
  }
  * { margin: 0; padding: 0; box-sizing: border-box; }
  html, body { width: 1200px; height: 900px; overflow: hidden; background: var(--page); }
  .canvas { position: relative; width: 1200px; height: 900px; }

  .label-band {
    position: absolute; left: 92px; top: 296px; width: 1021px; height: 375px;
    background:
      radial-gradient(circle at 92% 30%, rgba(255,255,255,0.45), transparent 28%),
      radial-gradient(circle at 30% 60%, rgba(180,150,220,0.35), transparent 45%),
      linear-gradient(100deg, var(--plum-deep), var(--plum) 45%, var(--plum-light) 100%);
  }
  .frames { position: absolute; left: 0; top: 0; }

  .serif { font-family: "Tinos", "Times New Roman", serif; }
  .txt { position: absolute; white-space: nowrap; }
  .center { transform: translateX(-50%); text-align: center; }

  .ingredients-title { left: 346px; top: 388px; font-size: 21px; color: var(--plum); }
  .ingredients-list { left: 346px; top: 415px; font-size: 17px; line-height: 26px; color: var(--plum); }
  .back-brand { left: 346px; top: 522px; font-size: 20px; color: var(--plum); }
  .back-web { left: 346px; top: 551px; font-size: 16.5px; color: var(--plum); }

  .company-title { left: 120px; top: 600px; font-size: 20px; color: var(--white); }
  .company-line { left: 120px; font-size: 14px; color: var(--white); }
  .company-line.one { top: 626px; }
  .company-line.two { top: 646px; }

  .brand-mark { left: 816px; top: 360px; display: flex; flex-direction: column; align-items: center; gap: 10px; }
  .brand-dot { width: 26px; height: 26px; border-radius: 50%; border: 1.5px solid var(--white); }
  .brand-name {
    font-family: "Josefin Sans", "Helvetica", sans-serif; font-weight: 300;
    font-size: 25px; letter-spacing: 3px; color: var(--white);
    border-top: 1px solid rgba(255,255,255,0.8); padding-top: 6px;
  }
  .tagline { left: 816px; top: 461px; font-size: 13.5px; letter-spacing: 0.4px; color: var(--white); }
  .product-name {
    left: 816px; top: 482px; font-family: "Playfair Display SC", "Georgia", serif;
    font-weight: 700; font-size: 50px; color: var(--white); letter-spacing: 1px;
  }
  .signature {
    left: 816px; top: 552px; font-family: "Great Vibes", cursive;
    font-size: 20px; line-height: 20px; color: rgba(255,255,255,0.85);
  }
  .volume { left: 1008px; top: 605px; font-size: 30px; color: var(--white); }
  .volume small { font-size: 17px; }
</style>
</head>
<body>
<div class="canvas">
  <div class="label-band" role="img" aria-label="Plum sequin glitter background pattern"></div>

  <svg class="frames" width="1200" height="900" viewBox="0 0 1200 900" aria-hidden="true">
    <path class="back-panel" fill="var(--panel)" stroke="var(--panel-edge)" stroke-width="2.5"
      d="M346,343 C360,362 380,372 410,374 L472,376 Q518,378 518,420 L518,534 Q518,576 472,578 L410,580 C380,584 360,592 346,606 C332,592 312,584 282,580 L220,578 Q174,576 174,534 L174,420 Q174,378 220,376 L282,374 C312,372 332,362 346,343 Z"/>
    <path class="front-bracket" fill="rgba(255,255,255,0.16)" stroke="var(--white)" stroke-width="13"
      d="M816,312 C835,340 860,352 900,356 L990,358 Q1034,360 1034,410 L1034,552 Q1034,600 990,602 L900,604 C860,608 835,620 816,646 C797,620 772,608 732,604 L642,602 Q598,600 598,552 L598,410 Q598,360 642,358 L732,356 C772,352 797,340 816,312 Z"/>
    <path class="front-bracket-inner" fill="none" stroke="rgba(200,200,210,0.9)" stroke-width="2"
      d="M816,324 C833,348 858,360 898,364 L988,366 Q1026,368 1026,412 L1026,550 Q1026,592 988,594 L898,596 C858,600 833,612 816,634 C799,612 774,600 734,596 L644,594 Q606,592 606,550 L606,412 Q606,368 644,366 L734,364 C774,360 799,348 816,324 Z"/>
  </svg>

  <div class="txt serif center ingredients-title">Ingredients:</div>
  <div class="txt serif center ingredients-list">Pure Lakns Djknf, Dwkhb<br>Kwd;jbc D/chkv Wdkcb</div>
  <div class="txt serif center back-brand">Corvina Brow</div>
  <div class="txt serif center back-web">www.corvinabrow.com</div>

  <div class="txt serif company-title">Company Details:</div>
  <div class="txt serif company-line one">2210 Harbor Street Suite #204</div>
  <div class="txt serif company-line two">Oakland, CA94607</div>

  <div class="txt center brand-mark">
    <span class="brand-dot"></span>
    <span class="brand-name">CORVINA BROW</span>
  </div>
  <div class="txt serif center tagline">Certified Medical Grade Low Fume Adhesive</div>
  <div class="txt center product-name">Lumen Soft</div>
  <div class="txt center signature">by<br>Marisol Everly</div>
  <div class="txt serif volume">10<small>ml</small></div>
</div>
</body>
</html>
```